A5 Flyers - 4 per page front and back - GlenmoorTrade

Design an A5 flyer (148 x 105mm) in Landscape mode. Allow 4 flyers to be printed per A4 sheet. Company logo and colours provided, along with the words. Designer required to provide a simple but striking design using the company colours, the rest is up to the designer. See further details in the attachments.

```html
<!DOCTYPE html>
<html lang="en">
<head>
<meta charset="utf-8">
<title>GlenmoorTrade A5 Flyer</title>
<link href="https://fonts.googleapis.com/css2?family=Oswald:wght@500;700&family=Questrial&display=swap" rel="stylesheet">
<style>
  :root{
    --orange:#f26b21;
    --navy:#243444;
    --ink:#2b2b2b;
    --white:#ffffff;
    --stage:#3b3b3b;
    --rule:#d9d9d9;
  }
  *{box-sizing:border-box;margin:0;padding:0}
  html,body{width:1200px;height:3600px;overflow:hidden}
  body{background:var(--stage);font-family:"Questrial",Arial,sans-serif;color:var(--ink);position:relative}
  .flyer{position:absolute;left:160px;width:880px;height:1300px;background:var(--white);overflow:hidden}
  .flyer--front{top:440px}
  .flyer--back{top:1860px}
  .shapes{position:absolute;inset:0;width:880px;height:1300px}
  .logo{position:absolute;font-family:"Oswald",Arial,sans-serif;font-weight:500;color:var(--orange);text-align:center;line-height:1}
  .logo__line{display:block}
  .logo--front{right:56px;top:70px;width:340px}
  .logo--front .logo__line:first-child{font-size:62px;letter-spacing:4px}
  .logo--front .logo__line:last-child{font-size:40px;letter-spacing:14px;margin-top:4px}
  .headline{position:absolute;font-family:"Oswald",Arial,sans-serif;font-weight:700;color:var(--white);text-transform:uppercase;line-height:1.12}
  .headline--front{left:440px;top:290px;font-size:56px}
  .headline--back{left:360px;top:28px;font-size:50px}
  .panel-text{position:absolute;color:var(--white);font-size:16.5px;line-height:1.32;text-align:justify}
  .panel-text p+p{margin-top:16px}
  .panel-text--front{left:440px;top:458px;width:410px}
  .panel-text--back{left:440px;top:285px;width:410px;font-size:15.5px;line-height:1.3}
  .panel-text--back p+p{margin-top:12px}
  .cost-box{position:absolute;left:48px;top:690px;width:372px;height:305px;background:var(--navy);padding:20px 26px;color:var(--white)}
  .cost-box__title{font-family:"Oswald",Arial,sans-serif;font-weight:700;color:var(--orange);font-size:28px;line-height:1.12;text-transform:uppercase}
  .cost-box__text{font-size:14.5px;line-height:1.28;margin-top:8px;text-align:justify}
  .cost-box__text+.cost-box__text{margin-top:10px}
  .accent{color:var(--orange)}
  .flow{position:absolute;left:425px;top:705px;width:440px;height:270px}
  .flow__label{font-family:"Questrial",Arial,sans-serif;font-size:9px;fill:#555}
  .features{position:absolute;left:48px;top:1018px;width:790px;display:flex;gap:30px}
  .feature{flex:1;border-top:2px solid var(--rule);padding-top:10px}
  .feature__head{display:flex;align-items:center;gap:8px;font-family:"Oswald",Arial,sans-serif;font-weight:700;color:var(--orange);font-size:22px;text-transform:uppercase}
  .feature__head svg{flex:0 0 auto}
  .feature__text{margin-top:10px;font-size:16px;line-height:1.3}
  .footer{position:absolute;left:0;bottom:0;width:880px;height:62px;background:var(--orange);display:flex;align-items:center;justify-content:space-between;padding:0 40px}
  .footer__url{font-family:"Oswald",Arial,sans-serif;font-weight:700;color:var(--white);font-size:26px}
  .footer__social{display:flex;gap:12px}
  .footer__social span{width:30px;height:30px;background:var(--white);border-radius:3px}
  .supply{position:absolute;left:48px;top:585px;width:380px}
  .supply__title{font-family:"Oswald",Arial,sans-serif;font-weight:700;color:var(--orange);font-size:34px;line-height:1.14;text-transform:uppercase}
  .supply__text{font-size:15px;font-weight:bold;line-height:1.3;margin-top:16px;color:#222}
  .sectors{position:absolute;left:48px;top:810px;width:370px;display:grid;grid-template-columns:1fr 1fr;gap:12px}
  .sector{position:relative;height:180px}
  .sector__photo{position:absolute;inset:0}
  .sector__label{position:absolute;left:0;right:0;bottom:0;background:var(--orange);color:var(--white);font-family:"Oswald",Arial,sans-serif;font-weight:700;font-size:14px;text-align:center;padding:4px 0;text-transform:uppercase}
  .suppliers{position:absolute;left:480px;top:585px;width:360px}
  .suppliers__title{font-family:"Oswald",Arial,sans-serif;font-weight:700;color:var(--orange);font-size:40px;line-height:1.1}
  .suppliers__lead{font-family:"Questrial",Arial,sans-serif;font-weight:bold;font-size:26px;line-height:1.2;color:#222;margin-top:4px}
  .suppliers__text{font-size:15px;font-weight:bold;line-height:1.32;margin-top:28px;color:#222}
  .suppliers__text+.suppliers__text{margin-top:22px}
  .logo--back{right:46px;top:1090px;width:320px}
  .logo--back .logo__line:first-child{font-size:60px;letter-spacing:4px}
  .logo--back .logo__line:last-child{font-size:38px;letter-spacing:13px;margin-top:4px}
</style>
</head>
<body>

<!-- Front side -->
<section class="flyer flyer--front">
  <svg class="shapes" viewBox="0 0 880 1300">
    <polygon points="220,20 700,640 0,640 0,300" fill="var(--orange)"/>
    <rect x="430" y="262" width="450" height="180" fill="var(--orange)"/>
    <rect x="430" y="442" width="450" height="250" fill="var(--navy)"/>
    <defs>
      <linearGradient id="mineGrad" x1="0" y1="0" x2="1" y2="1">
        <stop offset="0" stop-color="#7a6a5a"/>
        <stop offset="0.5" stop-color="#4d4a48"/>
        <stop offset="1" stop-color="#2e3136"/>
      </linearGradient>
    </defs>
    <polygon role="img" aria-label="Aerial photo of a bucket-wheel excavator at an open-pit mine" points="222,95 430,360 430,692 0,692 0,380" fill="url(#mineGrad)"/>
  </svg>

  <div class="logo logo--front"><span class="logo__line">GLENMOOR</span><span class="logo__line">TRADE</span></div>

  <h1 class="headline headline--front">We keep your<br>issue quiet</h1>

  <div class="panel-text panel-text--front">
    <p>A major mining company had a failure of a conveyor belt. The company had sourced a replacement belt, but this was weeks from being delivered, and the mining company could not afford extended downtime.</p>
    <p>Anonymously GlenmoorTrade advertised the requirement, and alternate sources of supply were quickly identified without the mining company needing to reveal their equipment failure. The mining company could then determine who they wanted to deal with and complete the transaction under their control.</p>
  </div>

  <div class="cost-box">
    <h2 class="cost-box__title">We can deliver<br>reduced cost</h2>
    <p class="cost-box__text">A crane boom replacement was listed on GlenmoorTrade to help source alternate suppliers. Three alternate compliant sources were located via the unique <span class="accent">GlenmoorTrade</span> broadcast system, leading to a cost reduction of 65% compared to the original quote received.</p>
    <p class="cost-box__text"><span class="accent">GlenmoorTrade</span> can find parts and equipment fast, but it can also find alternate sources of supply for hard to locate spare parts &amp; equipment or provide cheaper alternatives.</p>
  </div>

  <svg class="flow" viewBox="0 0 440 270" role="img" aria-label="Process flow from part failure to dispatch">
    <path d="M40 40 H400 A40 40 0 0 1 400 130 H40 A40 40 0 0 0 40 220 H400" fill="none" stroke="#bbb" stroke-width="2"/>
    <g fill="var(--white)" stroke="var(--orange)" stroke-width="2">
      <circle cx="60" cy="40" r="14"/><circle cx="220" cy="40" r="14"/><circle cx="380" cy="40" r="14"/>
      <circle cx="60" cy="130" r="14"/><circle cx="167" cy="130" r="14"/><circle cx="273" cy="130" r="14"/><circle cx="380" cy="130" r="14"/>
      <circle cx="60" cy="220" r="14"/><circle cx="220" cy="220" r="14"/><circle cx="380" cy="220" r="14"/>
    </g>
    <g fill="var(--navy)">
      <circle cx="60" cy="40" r="4"/><circle cx="220" cy="40" r="4"/><circle cx="380" cy="40" r="4"/>
      <circle cx="60" cy="130" r="4"/><circle cx="167" cy="130" r="4"/><circle cx="273" cy="130" r="4"/><circle cx="380" cy="130" r="4"/>
      <circle cx="60" cy="220" r="4"/><circle cx="220" cy="220" r="4"/><circle cx="380" cy="220" r="4"/>
    </g>
    <g class="flow__label" text-anchor="middle">
      <text x="60" y="68">Part fails on site</text>
      <text x="220" y="68">Request posted anonymously</text>
      <text x="380" y="68">Broadcast to members</text>
      <text x="60" y="158">Suppliers notified</text>
      <text x="167" y="158">Stock checked</text>
      <text x="273" y="158">Quotes returned</text>
      <text x="380" y="158">Sources matched</text>
      <text x="60" y="248">Buyer reviews offers</text>
      <text x="220" y="248">Supplier chosen privately</text>
      <text x="380" y="248">Part dispatched fast</text>
    </g>
  </svg>

  <div class="features">
    <div class="feature">
      <div class="feature__head">
        <svg width="24" height="24" viewBox="0 0 24 24"><circle cx="12" cy="10" r="6" fill="none" stroke="var(--orange)" stroke-width="2"/><rect x="9" y="17" width="6" height="4" fill="var(--orange)"/></svg>
        Unusual
      </div>
      <p class="feature__text">GlenmoorTrade is a unique and innovative service that brings a new perspective to the procurement of emergency spare parts and equipment.</p>
    </div>
    <div class="feature">
      <div class="feature__head">
        <svg width="24" height="24" viewBox="0 0 24 24" fill="var(--orange)"><circle cx="12" cy="5" r="3"/><circle cx="5" cy="17" r="3"/><circle cx="19" cy="17" r="3"/></svg>
        Socially simple
      </div>
      <p class="feature__text">We use technology to connect people and companies to new sources of supply that could be significantly closer than you may realise.</p>
    </div>
    <div class="feature">
      <div class="feature__head">
        <svg width="24" height="24" viewBox="0 0 24 24"><polyline points="8,5 15,12 8,19" fill="none" stroke="var(--orange)" stroke-width="3"/></svg>
        We don't tell...
      </div>
      <p class="feature__text">We won't tell the world that you have a problem. Your request will remain anonymous until you decide to provide your details.</p>
    </div>
  </div>

  <footer class="footer">
    <span class="footer__url">www.glenmoortrade.com</span>
    <span class="footer__social"><span></span><span></span><span></span></span>
  </footer>
</section>

<!-- Back side -->
<section class="flyer flyer--back">
  <svg class="shapes" viewBox="0 0 880 1300">
    <defs>
      <linearGradient id="truckGrad" x1="0" y1="0" x2="1" y2="1">
        <stop offset="0" stop-color="#6f8fb3"/>
        <stop offset="0.55" stop-color="#3e5573"/>
        <stop offset="1" stop-color="#1f2c3c"/>
      </linearGradient>
    </defs>
    <rect x="340" y="18" width="540" height="195" fill="var(--orange)"/>
    <rect x="0" y="213" width="880" height="335" fill="var(--navy)"/>
    <polygon role="img" aria-label="Photo of a truck with trailer driving on a highway at dusk" points="145,18 470,548 0,548 0,260" fill="url(#truckGrad)"/>
  </svg>

  <h1 class="headline headline--back">We can deliver<br>parts &amp; equipment<br>quicker</h1>

  <div class="panel-text panel-text--back">
    <p>A GlenmoorTrade member needed parts urgently due to a small fire. The parts were not in inventory, the manufacturer was overseas and difficult to contact due to holidays and time zones. Delivery from the manufacturer was finally determined as 3 weeks.</p>
    <p>GlenmoorTrade advertised the requirement anonymously, a member responded and the parts were delivered in 5 days. The applicable plant was returned on-line quicker and cheaper due to sharing and collaboration within and across industry.</p>
  </div>

  <div class="supply">
    <h2 class="supply__title">Can you help supply<br>an industrial<br>spare part?</h2>
    <p class="supply__text">If you are currently supplying industrial spare parts to the industries listed below, GlenmoorTrade will help you access an additional channel for your sales – all for free!</p>
  </div>

  <div class="sectors">
    <div class="sector"><div class="sector__photo" role="img" aria-label="Photo of an offshore oil and gas platform" style="background:linear-gradient(160deg,#7fa3c4,#3d5873)"></div><span class="sector__label">Oil &amp; Gas</span></div>
    <div class="sector"><div class="sector__photo" role="img" aria-label="Photo of wind turbines against the sky" style="background:linear-gradient(160deg,#c9d6e2,#8aa0b4)"></div><span class="sector__label">Power Generation</span></div>
    <div class="sector"><div class="sector__photo" role="img" aria-label="Photo of a large mining haul truck" style="background:linear-gradient(160deg,#9a9a9a,#4d4d4d)"></div><span class="sector__label">Mining</span></div>
    <div class="sector"><div class="sector__photo" role="img" aria-label="Photo of a factory production line" style="background:linear-gradient(160deg,#6e7fa8,#33405e)"></div><span class="sector__label">Manufacturing</span></div>
  </div>

  <div class="suppliers">
    <h2 class="suppliers__title">SUPPLIERS...</h2>
    <p class="suppliers__lead">Want to sell more spare parts? Want new sales leads and customers?</p>
    <p class="suppliers__text">GlenmoorTrade is building a network of suppliers that can meet the demand for industrial spare parts – fast.</p>
    <p class="suppliers__text">We're connecting suppliers with procurement, engineering or production professionals around the globe. Take advantage of our free registration period and be part of this innovative supply solution.</p>
  </div>

  <div class="logo logo--back"><span class="logo__line">GLENMOOR</span><span class="logo__line">TRADE</span></div>

  <footer class="footer">
    <span class="footer__url">www.glenmoortrade.com</span>
    <span class="footer__social"><span></span><span></span><span></span></span>
  </footer>
</section>

</body>
</html>
```